New Jazz Music Album CD Design

Need a contemporary jazz CD cover for my single I will be releasing December 31. Name of the song is called Velvet Drift . Artist Name is Dorian Mapes. Website is Http://DorianM.com. Please find a way to incorporate my attached logo and add my attached picture somewhere to the album art. Front Cover Demensions width 1423 pixel height 1411 pixels RGB 16 color no bleed. Inside Front Cover Demensions width 1423 pixel height 1411 pixels RGB 16 color no bleed. Disc dimensions Diameter: 1394 pixels RGB 16 bit color. Back tray card with 2 spines width (includes 2 spines) 1772 pixels height 1385 pixels spine width 74 pixels.
Updates

The images in the path below will also suffice for the design https://qkfiles.example/f/s!BtRZLMWc7WHMjoTt6ZI65SbxyQ4a

Target Market(s)

Age group 35 and older. Smooth jazz listeners.

Industry/Entity Type

Music Download

Font styles to use
Serif
Sans Serif

Colors

Designer to choose colors to be used in the design.

Requirements
Must have
• Song title Velvet Drift
• Artist name: Dorian M
• Attached Logo
• Website: DorianM.com
Nice to have
• NA
Should not have
• Na

```html
<!DOCTYPE html>
<html lang="en">
<head>
<meta charset="UTF-8">
<title>Velvet Drift — Dorian M</title>
<link rel="stylesheet" href="https://fonts.googleapis.com/css2?family=Montserrat:wght@700;800&family=Oswald:wght@400&display=swap">
<style>
  :root {
    --bg-indigo: #2f3192;
    --accent-blue: #4a6dff;
    --ink-white: #ffffff;
    --panel-grey: #666666;
    --logo-grey: #d9d9d9;
  }
  * { margin: 0; padding: 0; box-sizing: border-box; }
  html, body { width: 1200px; height: 1190px; overflow: hidden; }
  body { background: var(--bg-indigo); font-family: "Montserrat", Arial, sans-serif; }
  .cover { position: relative; width: 1200px; height: 1190px; background: var(--bg-indigo); overflow: hidden; }
  .headline { position: absolute; left: 0; top: 0; width: 1200px; height: 420px; }
  .headline .sans { font-family: "Montserrat", Arial, sans-serif; font-weight: 800; }
  .headline .tall { font-family: "Oswald", "Arial Narrow", sans-serif; font-weight: 400; }
  .artist-photo {
    position: absolute; left: 67px; top: 421px; width: 770px; height: 769px;
    background:
      radial-gradient(ellipse 32% 40% at 28% 75%, rgba(240,242,255,0.85), rgba(240,242,255,0) 70%),
      radial-gradient(ellipse 26% 55% at 72% 68%, rgba(170,185,255,0.55), rgba(170,185,255,0) 70%),
      radial-gradient(ellipse 20% 16% at 30% 18%, rgba(90,110,230,0.7), rgba(90,110,230,0) 75%),
      linear-gradient(180deg, rgba(47,49,146,0) 0%, rgba(40,42,150,0.6) 45%, rgba(35,38,140,0.8) 100%);
  }
  .site-panel {
    position: absolute; left: 921px; top: 812px; width: 237px; height: 378px;
    background: var(--panel-grey); padding: 26px 0 0 24px;
  }
  .site-url {
    color: var(--ink-white); font-weight: 800; font-size: 58px; line-height: 1.02;
    letter-spacing: -1px;
  }
  .logo-mark {
    position: absolute; left: 18px; bottom: 28px; display: flex; align-items: center; gap: 8px;
    color: var(--logo-grey); font-weight: 700; font-size: 30px; font-family: "Montserrat", Arial, sans-serif;
  }
  .logo-mark .dot { width: 14px; height: 14px; background: var(--logo-grey); }
</style>
</head>
<body>
<main class="cover">
  <svg class="headline" viewBox="0 0 1200 420" aria-label="Velvet Drift — Dorian M">
    <text class="sans" x="158" y="207" font-size="124" fill="var(--ink-white)" textLength="420" lengthAdjust="spacingAndGlyphs">VELVET</text>
    <text class="sans" x="158" y="303" font-size="124" fill="var(--accent-blue)" textLength="420" lengthAdjust="spacingAndGlyphs">DRIFT</text>
    <text class="tall" x="596" y="388" font-size="232" fill="var(--ink-white)">D</text>
    <text class="sans" x="702" y="388" font-size="110" fill="var(--ink-white)" textLength="440" lengthAdjust="spacingAndGlyphs">ORIAN M</text>
  </svg>

  <div class="artist-photo" role="img" aria-label="Blue-toned photo of the artist in a flat cap, white shirt and dark vest playing an alto saxophone"></div>

  <aside class="site-panel">
    <p class="site-url">DOR<br>IANM.<br>COM</p>
    <div class="logo-mark"><span class="dot"></span><span>Dorian M.</span></div>
  </aside>
</main>
</body>
</html>
```